Marketing One-Sheet for Security Deposit Claim Notice

I need a one-sheet flyer formatted for email distribution — optimized as a JPEG/PNG that I can insert into Constant Contact or Outlook. I do not want to attach it to an email, but insert it in the email we send out. I would like it to look professional but engaging. Some images would be good, but want to make sure it reads well if images do not load for the recipients. The text is in the attached Word document, but I am open to changes/ideas that may be better for marketing purposes. I included the URLs for some of the links I would like in the one-sheet that is clickable. The logo for the business is being uploaded on the Word document. Proposed text is also uploaded in a Word document. Thank you.

Target Market(s)

Landlords, Real Estate Agents, Property Managers

Industry/Entity Type

Legal

Requirements
Must have
• Professional but appealing design. The One-sheet is going to be placed in the body of emails, not as an attachment.
Nice to have
• Include our logo for the business and the web links please.
Should not have
• Images can be ok, but it needs to look right if images do not download from the email sent out.

```html
<!DOCTYPE html>
<html lang="en">
<head>
<meta charset="UTF-8">
<title>Security Deposit Claim Notice</title>
<link href="https://fonts.googleapis.com/css2?family=Arimo:wght@400;700&display=swap" rel="stylesheet">
<style>
  :root {
    --red: #a8141e;
    --ink: #1e1e1e;
    --grey-frame: #a9a9a9;
    --grey-button: #464646;
    --link: #2b2f8f;
    --paper: #ffffff;
  }
  * { margin: 0; padding: 0; box-sizing: border-box; }
  html, body {
    width: 1200px; height: 1200px; overflow: hidden;
    background: var(--paper);
    font-family: "Arimo", Arial, sans-serif;
    color: var(--ink);
  }
  .sheet { position: relative; width: 1200px; height: 1200px; }
  .frame-outer {
    position: absolute; left: 16px; top: 155px; width: 1178px; height: 895px;
    border: 3px solid var(--red);
  }
  .frame-inner {
    position: absolute; left: 30px; top: 169px; width: 1150px; height: 867px;
    border: 3px solid var(--grey-frame);
  }
  .abs { position: absolute; white-space: nowrap; }
  .title {
    left: 0; width: 1200px; top: 196px; text-align: center;
    font-size: 50px; font-weight: 700; color: var(--red); letter-spacing: 0.5px;
  }
  .subtitle {
    left: 0; width: 1200px; top: 254px; text-align: center; font-size: 30px;
  }
  .col-heading { font-size: 28px; font-weight: 700; line-height: 34px; }
  .col-left { left: 66px; top: 330px; }
  .col-right { left: 627px; top: 330px; }
  .bullets { list-style: none; font-size: 24px; }
  .bullets li { position: relative; padding-left: 30px; }
  .bullets li::before {
    content: ""; position: absolute; left: 5px; top: 11px;
    width: 7px; height: 7px; border-radius: 50%; background: var(--ink);
  }
  .bullets-left { left: 66px; top: 417px; }
  .bullets-left li { margin-bottom: 16px; }
  .bullets-right { left: 620px; top: 405px; line-height: 28px; }
  .bullets-right li { margin-bottom: 17px; text-transform: none; }
  .body-copy {
    left: 61px; top: 565px; width: 1090px; white-space: normal;
    font-size: 22px; line-height: 28px;
  }
  .body-copy .accent { color: var(--red); }
  .fee {
    left: 0; width: 1200px; top: 700px; text-align: center;
    font-size: 56px; font-weight: 700; color: var(--red);
  }
  .fee .was { font-size: 28px; margin-left: 38px; vertical-align: 2px; }
  .fee-note { left: 0; width: 1200px; top: 766px; text-align: center; font-size: 28px; }
  .btn {
    position: absolute; display: flex; align-items: center; justify-content: center;
    color: #fff; font-weight: 700; font-size: 24px; text-align: center; line-height: 31px;
    text-decoration: none;
  }
  .btn-info { left: 79px; top: 822px; width: 513px; height: 64px; background: var(--red); }
  .btn-contact { left: 624px; top: 817px; width: 494px; height: 79px; background: var(--grey-button); }
  .brand { left: 87px; top: 898px; width: 215px; text-align: center; color: var(--red); font-weight: 700; }
  .brand-name { display: flex; align-items: center; gap: 6px; font-size: 25px; line-height: 28px; white-space: normal; text-align: left; }
  .brand-square { flex: none; width: 22px; height: 22px; background: var(--red); }
  .brand-tagline { font-size: 8px; line-height: 10px; margin-top: 6px; }
  .brand-web { font-size: 14px; margin-top: 2px; }
  .brand-phone { font-size: 14px; }
  .link { font-size: 22px; color: var(--link); text-decoration: underline; }
  .icon { position: absolute; }
</style>
</head>
<body>
<main class="sheet">
  <div class="frame-outer"></div>
  <div class="frame-inner"></div>

  <h1 class="abs title">SECURITY DEPOSIT CLAIM NOTICE</h1>
  <p class="abs subtitle">Landlord, need to keep the Security Deposit?</p>

  <h2 class="abs col-heading col-left">Security Deposit Claim Notice<br>requirements:</h2>
  <ul class="abs bullets bullets-left">
    <li>Must be served on time</li>
    <li>Must be served acording Florida law</li>
    <li>Must contain specific wording</li>
  </ul>

  <h2 class="abs col-heading col-right">Security Claim Notice not<br>correct, then:</h2>
  <ul class="abs bullets bullets-right">
    <li>tenant could demand return of FULL<br>&nbsp;&nbsp;SECURITY DEPOSIT</li>
    <li>tenant can sue and recover LEGAL FEES<br>FROM THE LANDLORD</li>
  </ul>

  <p class="abs body-copy">There are lawyers that specialize to representing <span class="accent">TENNTS</span> against landlords for not making proper claim on the security deposit. They can win the case and recover thousands of $ in legal fees from Landlord. Plus, tenant can get back 100% of the Security Deposit, even if they damaged the unit, if the Security Deposit Claim Notice is not served on time and correctly.</p>

  <p class="abs fee">FLAT FEE $350<span class="was">$450</span></p>
  <p class="abs fee-note">to prepare and serve Security Deposit Claim Notices for Landorks</p>

  <a class="btn btn-info" href="#">Want more information, CLICK HERE</a>
  <a class="btn btn-contact" href="#">Contact Us to prepare the<br>Secusit Claim Notice</a>

  <div class="abs brand">
    <div class="brand-name"><span>Tenancy Legal Group</span><span class="brand-square"></span></div>
    <div class="brand-tagline">A Legal Partner for Landlords<br>&amp; Property Managers</div>
    <div class="brand-web">TenancyLegalGroup.com</div>
    <div class="brand-phone">1(800) 555-0142</div>
  </div>

  <svg class="icon" style="left:326px;top:932px" width="24" height="24" viewBox="0 0 24 24" aria-hidden="true">
    <path d="M12 1v22M1 12h22" stroke="var(--red)" stroke-width="3"/>
  </svg>
  <a class="abs link" style="left:377px;top:935px" href="#">more information</a>

  <svg class="icon" style="left:330px;top:980px" width="24" height="19" viewBox="0 0 24 19" aria-hidden="true">
    <rect x="1.5" y="1.5" width="21" height="16" fill="none" stroke="var(--red)" stroke-width="3"/>
    <path d="M2 3l10 8 10-8" fill="none" stroke="var(--red)" stroke-width="3"/>
  </svg>
  <a class="abs link" style="left:379px;top:976px" href="#">request our hiring documents/</a>

  <svg class="icon" style="left:632px;top:912px" width="36" height="44" viewBox="0 0 36 44" aria-hidden="true">
    <path d="M2 2l30 26H19l9 13-5 2-9-13-10 9z" fill="#fff" stroke="var(--red)" stroke-width="2.5" stroke-linejoin="round"/>
  </svg>
  <a class="abs link" style="left:690px;top:935px" href="#">request our hiring documents/</a>
</main>
</body>
</html>
```